Cybersecurity company is looking for business card.

I need a business card design for our company, we are a cybersecurity company providing advance technology to protect agains any kind of malware. We need a fresh modern design it should communicate modern, technology and growth.

Target Market(s)

Business to business

Industry/Entity Type

Business

Contact Information for Business Card

Should have location, address, fax, mobile, phone, email and website.

Requirements
Must have
• Must follow company's logo color and style. Must have the company's log on its.

```html
<!DOCTYPE html>
<html lang="en">
<head>
<meta charset="utf-8">
<title>Vantrel Business Card</title>
<link rel="stylesheet" href="https://fonts.googleapis.com/css2?family=Arimo:wght@400;700&display=swap">
<style>
  :root {
    --brand-red: #c0202d;
    --brand-red-deep: #9a1620;
    --ink: #1e1e1e;
    --paper: #ffffff;
    --paper-shade: #ececec;
    --backdrop: #e7e4df;
    --muted: #3a3a3a;
  }
  * { box-sizing: border-box; margin: 0; padding: 0; }
  html, body {
    width: 1200px; height: 892px; overflow: hidden;
    background: var(--backdrop);
    font-family: "Arimo", Arial, sans-serif;
  }
  .stage {
    position: relative; width: 1200px; height: 892px;
    display: flex; align-items: center; justify-content: center; gap: 60px;
  }
  .card {
    position: relative; width: 530px; height: 303px;
    border-radius: 4px; overflow: hidden;
    box-shadow: 0 10px 28px rgba(0,0,0,.18);
  }
  /* Front */
  .card-front { background: var(--brand-red); }
  .front-shape { position: absolute; inset: 0; width: 100%; height: 100%; }
  .front-brand {
    position: absolute; left: 40px; top: 70px;
    display: flex; align-items: center; gap: 10px;
  }
  .brand-mark { width: 12px; height: 12px; background: var(--brand-red); }
  .brand-name {
    font-weight: 700; font-size: 70px; letter-spacing: 1px;
    color: var(--ink); line-height: 1;
  }
  .front-location {
    position: absolute; left: 52px; top: 150px;
    display: flex; align-items: center; gap: 6px;
    font-size: 15px; color: var(--muted);
  }
  .front-location svg { width: 10px; height: 14px; }
  .contact-list {
    position: absolute; left: 52px; top: 184px;
    list-style: none; font-size: 13px; color: var(--muted);
  }
  .contact-list li {
    display: flex; align-items: center; gap: 8px; height: 19px;
  }
  .contact-icon {
    width: 13px; height: 13px; background: var(--ink); border-radius: 2px;
    display: flex; align-items: center; justify-content: center;
  }
  .contact-icon svg { width: 9px; height: 9px; }
  .front-address {
    position: absolute; right: 22px; top: 26px;
    text-align: right; font-size: 13px; line-height: 1.45; color: var(--paper);
  }
  /* Back */
  .card-back {
    background: linear-gradient(135deg, var(--brand-red-deep) 0%, var(--brand-red) 55%, #a81a25 100%);
    display: flex; align-items: center; justify-content: center;
  }
  .card-back .brand-name { color: var(--paper); font-size: 86px; }
</style>
</head>
<body>
<main class="stage">
  <section class="card card-front" aria-label="Business card front">
    <svg class="front-shape" viewBox="0 0 530 303" preserveAspectRatio="none" aria-hidden="true">
      <path d="M0 0 H318 C412 58 446 178 430 303 H0 Z" fill="#111"/>
      <path d="M0 0 H306 C398 58 432 178 418 303 H0 Z" fill="#fff"/>
      <path d="M0 0 H296 C386 58 420 178 406 303 H0 Z" fill="url(#paperGrad)"/>
      <defs>
        <linearGradient id="paperGrad" x1="0" y1="0" x2="1" y2="1">
          <stop offset="0" stop-color="#ffffff"/>
          <stop offset="1" stop-color="#ececec"/>
        </linearGradient>
      </defs>
    </svg>
    <div class="front-address">Harbor Tech Park (HTP)<br>-Meridian Avenue</div>
    <div class="front-brand">
      <span class="brand-mark"></span>
      <span class="brand-name">vantrel</span>
    </div>
    <div class="front-location">
      <svg viewBox="0 0 10 14"><path d="M5 0a5 5 0 0 1 5 5c0 4-5 9-5 9S0 9 0 5a5 5 0 0 1 5-5z" fill="#c0202d"/><circle cx="5" cy="5" r="1.8" fill="#fff"/></svg>
      Lakeport - Avalon
    </div>
    <ul class="contact-list">
      <li><span class="contact-icon"><svg viewBox="0 0 10 10"><path d="M2 1l2 2-1 1.5c.7 1.3 1.2 1.8 2.5 2.5L7 6l2 2-1.5 1.5C4 9 1 6 .5 2.5z" fill="#fff"/></svg></span>05 246 XXXX</li>
      <li><span class="contact-icon"><svg viewBox="0 0 10 10"><rect x="1" y="3" width="8" height="5" fill="#fff"/><rect x="3" y="1" width="4" height="2" fill="#fff"/></svg></span>05 246 XXXX</li>
      <li><span class="contact-icon"><svg viewBox="0 0 10 10"><rect x="3" y="0.5" width="4" height="9" rx="1" fill="#fff"/></svg></span>+44 77 246 XXXX</li>
      <li><span class="contact-icon"><svg viewBox="0 0 10 10"><circle cx="5" cy="5" r="3.8" fill="none" stroke="#fff"/><path d="M1.2 5h7.6M5 1.2v7.6" stroke="#fff"/></svg></span>www.vantrel.com</li>
      <li><span class="contact-icon"><svg viewBox="0 0 10 10"><rect x="1" y="2" width="8" height="6" fill="#fff"/><path d="M1 2l4 3.5L9 2" fill="none" stroke="#1e1e1e"/></svg></span>name.surname@vantrel.com</li>
    </ul>
  </section>

  <section class="card card-back" aria-label="Business card back">
    <span class="brand-name">vantrel</span>
  </section>
</main>
</body>
</html>
```